Bramble Hollow Networks - Electrical

We need flyers for electrical services.
Areas of work include new builds, office fitouts, switchboard upgrades, installation of ceiling fans, powerpoint and downlight upgrades, home theatre and AV systems, all exterior and emergency work. Free quotes
We would like to see designs with the colour Red with a young and modern design. Licence No: 63914K must be included and call Leopold on 0438917062.

Colors
ec1f27

```html
<!DOCTYPE html>
<html lang="en">
<head>
<meta charset="utf-8">
<title>Bramble Hollow Networks – Electrical Flyer</title>
<link href="https://fonts.googleapis.com/css2?family=Montserrat:wght@400;500;700;800;900&family=Raleway:wght@400;700&display=swap" rel="stylesheet">
<style>
  :root {
    --red: #ec1f27;
    --red-deep: #a80f17;
    --yellow: #ffd400;
    --white: #ffffff;
    --bar-top: #3a3a3a;
    --bar-bottom: #0d0d0d;
  }
  * { margin: 0; padding: 0; box-sizing: border-box; }
  html, body { width: 857px; height: 1200px; overflow: hidden; background: var(--white); }
  .flyer {
    position: relative;
    width: 857px;
    height: 1200px;
    overflow: hidden;
    font-family: "Raleway", "Montserrat", sans-serif;
    color: var(--white);
    background: radial-gradient(ellipse at 40% 55%, var(--red) 0%, #d8161e 55%, var(--red-deep) 100%);
  }
  .hero-photo {
    position: absolute; left: 0; top: 0; width: 857px; height: 520px;
    background: linear-gradient(160deg, #e9e6e2 0%, #c9c2bb 35%, #3d4a78 62%, #26305a 80%, #d9d9d9 100%);
  }
  .backdrop { position: absolute; left: 0; top: 0; width: 857px; height: 1200px; }
  .brand { position: absolute; left: 26px; top: 522px; font-family: "Montserrat", sans-serif; }
  .brand__name { font-weight: 900; font-size: 42px; line-height: 1.05; color: var(--white); letter-spacing: 0.3px; }
  .brand__sub { font-weight: 800; font-size: 27px; line-height: 1.25; color: var(--yellow); }
  .intro {
    position: absolute; left: 26px; top: 636px; width: 370px;
    font-size: 15.5px; line-height: 24px;
  }
  .services { position: absolute; left: 24px; top: 722px; font-family: "Montserrat", sans-serif; }
  .services__title { font-weight: 700; font-size: 27px; color: var(--yellow); margin-bottom: 8px; }
  .services__list { list-style: none; }
  .services__list li {
    position: relative; padding-left: 26px; font-weight: 400; font-size: 19.5px; line-height: 32px;
  }
  .services__list li::before {
    content: ""; position: absolute; left: 4px; top: 11px; width: 11px; height: 11px;
    border-radius: 50%; background: var(--yellow);
  }
  .address {
    position: absolute; left: 26px; top: 1020px; width: 400px;
    font-family: "Montserrat", sans-serif; font-size: 19px; line-height: 26px;
  }
  .licence {
    position: absolute; left: 26px; top: 1080px;
    font-family: "Montserrat", sans-serif; font-weight: 700; font-size: 19px;
  }
  .about {
    position: absolute; left: 446px; top: 578px; width: 392px;
    font-size: 15.5px; line-height: 24px; text-align: justify;
  }
  .about strong { color: var(--yellow); font-weight: 700; }
  .gallery {
    position: absolute; left: 446px; top: 840px; width: 402px;
    display: grid; grid-template-columns: 197px 197px; grid-auto-rows: 133px; gap: 7px;
  }
  .gallery__photo { border: 2px solid var(--white); }
  .gallery__photo--fan { background: linear-gradient(150deg, #f1f1f1, #c8c6c4 60%, #8a8582); }
  .gallery__photo--aircon { background: linear-gradient(150deg, #e8eef1, #bcc7cc 55%, #5a6d8c); }
  .gallery__photo--board { background: linear-gradient(150deg, #9ba0a2, #5e5d5b 55%, #c46a2c); }
  .gallery__photo--cabling { background: linear-gradient(150deg, #d9d9d6, #b9b6b0 50%, #e0522a); }
  .callbar {
    position: absolute; left: 0; top: 1120px; width: 857px; height: 80px;
    background: linear-gradient(180deg, var(--bar-top), var(--bar-bottom));
    display: flex; align-items: center; justify-content: center;
    font-family: "Montserrat", sans-serif; font-weight: 700; font-size: 36px; letter-spacing: 0.5px;
  }
  .callbar__number { color: var(--yellow); margin-left: 12px; }
</style>
</head>
<body>
<main class="flyer">
  <div class="hero-photo" role="img" aria-label="Photo of an electrician in blue overalls testing wiring with a multimeter while a homeowner sits on a sofa behind"></div>

  <svg class="backdrop" viewBox="0 0 857 1200" aria-hidden="true">
    <defs>
      <linearGradient id="waveGold" x1="0" y1="0" x2="1" y2="0">
        <stop offset="0" stop-color="#f7c21a"/>
        <stop offset="0.5" stop-color="#ffd400"/>
        <stop offset="1" stop-color="#e9a80e"/>
      </linearGradient>
      <radialGradient id="sealFill" cx="0.4" cy="0.35" r="0.7">
        <stop offset="0" stop-color="#fbe08a"/>
        <stop offset="0.6" stop-color="#e2a51b"/>
        <stop offset="1" stop-color="#a8710a"/>
      </radialGradient>
    </defs>
    <path d="M0 410 C 200 390, 380 470, 600 500 C 700 512, 790 470, 857 440 L 857 1200 L 0 1200 Z" fill="url(#waveGold)"/>
    <path d="M0 428 C 200 410, 380 490, 600 522 C 700 534, 790 492, 857 462 L 857 1200 L 0 1200 Z" fill="var(--red)"/>
    <g class="seal">
      <circle cx="722" cy="465" r="90" fill="#c68c12"/>
      <circle cx="722" cy="465" r="84" fill="url(#sealFill)"/>
      <circle cx="722" cy="465" r="58" fill="#2a2a2a"/>
      <circle cx="722" cy="465" r="36" fill="url(#sealFill)"/>
    </g>
  </svg>

  <header class="brand">
    <h1 class="brand__name">BRAMBLE HOLLOW</h1>
    <p class="brand__sub">NETWORKS</p>
  </header>

  <p class="intro">Licensed electricians delivering safe, tidy and reliable work for homes and businesses across the region.</p>

  <section class="services">
    <h2 class="services__title">Areas of work</h2>
    <ul class="services__list">
      <li>New builds</li>
      <li>Office fitouts</li>
      <li>Switchboard upgrades</li>
      <li>Installation of ceiling fans</li>
      <li>Powerpoint and downlight upgrades,</li>
      <li>Home theatre and AV systems,</li>
      <li>All exterior and emergency work</li>
    </ul>
  </section>

  <p class="address">Adress Here Adress Here Adress Here Adress Here</p>
  <p class="licence">Licence No: 63914K</p>

  <section class="about">
    <p>Bramble Hollow Networks is a young, modern electrical team that treats every home and workplace with care. We turn up on time, explain the job and leave the site clean. <strong>Free quotes on every job, with clear pricing and no hidden costs. Ask us today.</strong></p>
    <p>Our electricians are fully licensed and insured, and we stand behind every installation we complete. From a new build to an urgent repair, one call gets it sorted.</p>
  </section>

  <div class="gallery">
    <div class="gallery__photo gallery__photo--fan" role="img" aria-label="Photo of an electrician installing a ceiling fan"></div>
    <div class="gallery__photo gallery__photo--aircon" role="img" aria-label="Photo of a technician servicing a wall-mounted air conditioner"></div>
    <div class="gallery__photo gallery__photo--board" role="img" aria-label="Photo of electricians working at a switchboard"></div>
    <div class="gallery__photo gallery__photo--cabling" role="img" aria-label="Photo of orange conduit cabling in a wall cavity"></div>
  </div>

  <footer class="callbar">CALL LEOPOLD ON<span class="callbar__number">0438917062</span></footer>
</main>
</body>
</html>
```